Infographic and content adjustment

For this project, the website content and the templates are already in place. We would need a professional placement of the content into the website, with appropriate and modern icons and/or high Res photos. The website "plenvoria.com" provides service to industry or social associations.

We like to see designs on below two templates to be able to compare. A template is already in place on
www.plenvoria.com/new

The second template would be:
www.plenvoria.com/new2

We would like to receive designs on both templates, so that we can choose the best.

The designer can use the attached power point content, revise the wording if needed and propose a professional design of those contents in the current template. High Res version of the pictures will be provided if necessary.

Target Market(s)

associations, their members,

Industry/Entity Type

Industry

Requirements
Must have
• easy and fast navigation, relevant icons and pictures, short and direct message.

```html
<!DOCTYPE html>
<html lang="en">
<head>
<meta charset="utf-8">
<title>Plenvoria – Association Testimonials and Membership Plans</title>
<link href="https://fonts.googleapis.com/css2?family=Roboto:wght@300;400&family=Roboto+Condensed:wght@300&display=swap" rel="stylesheet">
<style>
  :root {
    --bg-deep: #0c1c2c;
    --bg-top: #164a75;
    --band-top: #0a72ad;
    --band-bottom: #063d66;
    --card-blue: #0a6ba6;
    --plan-head: #050f1a;
    --plan-body: #0f2134;
    --accent: #33e0b2;
    --accent-soft: #5fd8b0;
    --white: #ffffff;
    --button-green: #5cb85c;
    --cta-blue-top: #2d8fc9;
    --cta-blue-bottom: #0e5a92;
    --footer: #2b3d50;
    --icon-grey: #bfc4c9;
  }
  * { margin: 0; padding: 0; box-sizing: border-box; }
  html, body { width: 1200px; height: 982px; overflow: hidden; }
  body {
    position: relative;
    font-family: Arial, Helvetica, sans-serif;
    color: var(--white);
    background: var(--bg-deep);
  }
  .testimonials {
    position: absolute; left: 0; top: 0; width: 1200px; height: 429px;
    background: linear-gradient(180deg, var(--bg-top) 0%, #113a5d 55%, var(--bg-deep) 100%);
  }
  .section-title {
    position: absolute; left: 0; width: 1200px; top: 30px; text-align: center;
    font-family: "Roboto", sans-serif; font-weight: 300; font-size: 33px;
    color: var(--accent); letter-spacing: 0.3px; line-height: 38px;
  }
  .section-subtitle {
    position: absolute; left: 0; width: 1200px; top: 69px; text-align: center;
    font-family: "Roboto Condensed", sans-serif; font-weight: 300; font-size: 18.5px;
    color: #e4edf4;
  }
  .testimonial-card {
    position: absolute; top: 167px; width: 174px; height: 228px;
    background: var(--card-blue); border-radius: 4px; text-align: center;
    box-shadow: 0 3px 6px rgba(0,0,0,0.25);
  }
  .client-badge {
    position: absolute; left: 46px; top: -42px; width: 82px; height: 82px;
    border-radius: 50%; background: var(--white);
    display: flex; align-items: center; justify-content: center;
    font-family: Arial, Helvetica, sans-serif; font-weight: 700; font-size: 13px;
    color: #1f8fd6;
  }
  .quote {
    position: absolute; left: 6px; right: 6px; top: 55px;
    font-size: 10.6px; line-height: 17.2px;
  }
  .author {
    position: absolute; left: 0; right: 0; top: 364px; top: 197px;
    font-size: 10.6px; color: var(--accent-soft);
  }
  .pricing {
    position: absolute; left: 0; top: 429px; width: 1200px; height: 393px;
    background: linear-gradient(180deg, var(--band-top) 0%, #085b92 60%, var(--band-bottom) 100%);
  }
  .plan-card {
    position: absolute; top: 16px; width: 174px; height: 356px;
    background: var(--plan-body); border-radius: 4px; overflow: hidden; text-align: center;
    box-shadow: 0 4px 8px rgba(0,0,0,0.35);
  }
  .plan-name {
    height: 45px; line-height: 47px; background: var(--plan-head);
    font-family: "Roboto", sans-serif; font-weight: 300; font-size: 17px; color: var(--accent);
  }
  .plan-price {
    margin-top: 20px; font-family: "Roboto", sans-serif; font-weight: 300; font-size: 18px;
  }
  .plan-audience { margin-top: 4px; font-size: 10.6px; color: var(--accent); }
  .plan-features { list-style: none; margin-top: 14px; font-size: 10.5px; }
  .plan-features li { height: 26px; line-height: 26px; }
  .sign-up {
    position: absolute; left: 56px; top: 307px; width: 61px; height: 26px;
    border-radius: 4px; background: var(--button-green);
    font-size: 10.5px; line-height: 26px; color: var(--white);
  }
  .cta {
    position: absolute; left: 0; top: 822px; width: 1200px; height: 110px;
    background: linear-gradient(180deg, #0d2f4c 0%, var(--bg-deep) 100%);
  }
  .cta-line {
    position: absolute; left: 226px; top: 51px; transform: translateY(-50%);
    font-family: "Roboto", sans-serif; font-weight: 300; font-size: 33.5px; color: var(--white);
  }
  .cta-line .highlight { color: var(--accent-soft); }
  .cta-button {
    position: absolute; left: 720px; top: 32px; width: 249px; height: 48px;
    border-radius: 4px; background: linear-gradient(180deg, var(--cta-blue-top), var(--cta-blue-bottom));
    text-align: center; line-height: 48px;
    font-family: "Roboto Condensed", sans-serif; font-weight: 300; font-size: 25px;
  }
  .site-footer {
    position: absolute; left: 0; top: 932px; width: 1200px; height: 50px; background: var(--footer);
  }
  .copyright { position: absolute; left: 199px; top: 19px; font-size: 10px; }
  .social-links { position: absolute; left: 795px; top: 13px; display: flex; gap: 3px; }
  .social-icon {
    width: 24px; height: 24px; border-radius: 50%; background: var(--icon-grey);
    display: flex; align-items: center; justify-content: center;
  }
  .social-icon svg { width: 14px; height: 14px; }
</style>
</head>
<body>
  <section class="testimonials">
    <h1 class="section-title">TESTIMONIALS</h1>
    <p class="section-subtitle">See what our clients says</p>

    <article class="testimonial-card" style="left:196px">
      <div class="client-badge">Brandwell</div>
      <p class="quote">“Donec hendrerit nibh ac augue pretium, eget imperdiet odio sagittis. Sed vulputate hendrerit sapien, quis cursus turpis sollicitudin vel. Sed eleifend purus quis felis dignissim tempus. ”</p>
      <p class="author">Tom Reyes, CEO Brandwell</p>
    </article>
    <article class="testimonial-card" style="left:401px">
      <div class="client-badge">Brandwell</div>
      <p class="quote">“Donec hendrerit nibh ac augue pretium, eget imperdiet odio sagittis. Sed vulputate hendrerit sapien, quis cursus turpis sollicitudin vel. Sed eleifend purus quis felis dignissim tempus. ”</p>
      <p class="author">Tom Reyes, CEO Brandwell</p>
    </article>
    <article class="testimonial-card" style="left:606px">
      <div class="client-badge">Brandwell</div>
      <p class="quote">“Donec hendrerit nibh ac augue pretium, eget imperdiet odio sagittis. Sed vulputate hendrerit sapien, quis cursus turpis sollicitudin vel. Sed eleifend purus quis felis dignissim tempus. ”</p>
      <p class="author">Tom Reyes, CEO Brandwell</p>
    </article>
    <article class="testimonial-card" style="left:811px">
      <div class="client-badge">Brandwell</div>
      <p class="quote">“Donec hendrerit nibh ac augue pretium, eget imperdiet odio sagittis. Sed vulputate hendrerit sapien, quis cursus turpis sollicitudin vel. Sed eleifend purus quis felis dignissim tempus. ”</p>
      <p class="author">Tom Reyes, CEO Brandwell</p>
    </article>
  </section>

  <section class="pricing">
    <article class="plan-card" style="left:196px">
      <h2 class="plan-name">Starter</h2>
      <p class="plan-price">$30/mo</p>
      <p class="plan-audience">single association</p>
      <ul class="plan-features">
        <li>1 Month FREE Trial</li><li>1 Project</li><li>Import File</li><li>Public Database</li><li>Basic Reports</li>
      </ul>
      <div class="sign-up">Sign Up</div>
    </article>
    <article class="plan-card" style="left:401px">
      <h2 class="plan-name">Starter</h2>
      <p class="plan-price">$55/mo</p>
      <p class="plan-audience">small associations</p>
      <ul class="plan-features">
        <li>1 Month FREE Trial</li><li>5 Projects</li><li>Import File</li><li>Public Database</li><li>Built-in Analytics</li>
      </ul>
      <div class="sign-up">Sign Up</div>
    </article>
    <article class="plan-card" style="left:606px">
      <h2 class="plan-name">Starter</h2>
      <p class="plan-price">$90/mo</p>
      <p class="plan-audience">association networks/analysts</p>
      <ul class="plan-features">
        <li>1 Month FREE Trial</li><li>20 Projects</li><li>Import File</li><li>Public Database</li><li>Advanced Analytics</li><li>Customizable Visual Views</li>
      </ul>
      <div class="sign-up">Sign Up</div>
    </article>
    <article class="plan-card" style="left:811px">
      <h2 class="plan-name">Starter</h2>
      <p class="plan-price">$150/mo</p>
      <p class="plan-audience">industry federations</p>
      <ul class="plan-features">
        <li>1 Month FREE Trial</li><li>100 Projects</li><li>Import File</li><li>Public Database</li><li>Advanced Analytics</li><li>Customizable Visual Views</li><li>Customization and Sharing</li>
      </ul>
      <div class="sign-up">Sign Up</div>
    </article>
  </section>

  <section class="cta">
    <p class="cta-line">Why not give a try, <span class="highlight">for free.</span></p>
    <div class="cta-button">TRY IT OUT</div>
  </section>

  <footer class="site-footer">
    <p class="copyright">© 2014 PLENVORIA, ALL RIGHTS RESERVED</p>
    <nav class="social-links" aria-label="Contact and sharing links">
      <span class="social-icon" aria-label="Email"><svg viewBox="0 0 14 14"><rect x="1.5" y="3" width="11" height="8" rx="1" fill="none" stroke="#fff" stroke-width="1.4"/><path d="M1.8 3.5 7 7.6l5.2-4.1" fill="none" stroke="#fff" stroke-width="1.4"/></svg></span>
      <span class="social-icon" aria-label="Phone"><svg viewBox="0 0 14 14"><path d="M3 1.8h2.2l1 2.6-1.4 1a7 7 0 0 0 3.8 3.8l1-1.4 2.6 1v2.2a1 1 0 0 1-1 1A10 10 0 0 1 2 2.8a1 1 0 0 1 1-1z" fill="#fff"/></svg></span>
      <span class="social-icon" aria-label="Location"><svg viewBox="0 0 14 14"><path d="M7 1.2a4 4 0 0 1 4 4c0 3-4 7.6-4 7.6S3 8.2 3 5.2a4 4 0 0 1 4-4z" fill="#fff"/><circle cx="7" cy="5.2" r="1.4" fill="#bfc4c9"/></svg></span>
      <span class="social-icon" aria-label="Chat"><svg viewBox="0 0 14 14"><path d="M2 2.5h10a1 1 0 0 1 1 1v5.5a1 1 0 0 1-1 1H6l-3 2.5V10H2a1 1 0 0 1-1-1V3.5a1 1 0 0 1 1-1z" fill="#fff"/></svg></span>
      <span class="social-icon" aria-label="Share"><svg viewBox="0 0 14 14"><circle cx="3.5" cy="7" r="1.8" fill="#fff"/><circle cx="10.5" cy="3" r="1.8" fill="#fff"/><circle cx="10.5" cy="11" r="1.8" fill="#fff"/><path d="M3.5 7 10.5 3M3.5 7l7 4" stroke="#fff" stroke-width="1.3"/></svg></span>
      <span class="social-icon" aria-label="Website"><svg viewBox="0 0 14 14"><circle cx="7" cy="7" r="5.3" fill="none" stroke="#fff" stroke-width="1.3"/><ellipse cx="7" cy="7" rx="2.3" ry="5.3" fill="none" stroke="#fff" stroke-width="1.1"/><path d="M1.7 7h10.6" stroke="#fff" stroke-width="1.1"/></svg></span>
      <span class="social-icon" aria-label="Link"><svg viewBox="0 0 14 14"><rect x="1.5" y="5" width="6.5" height="4" rx="2" fill="none" stroke="#fff" stroke-width="1.4"/><rect x="6" y="5" width="6.5" height="4" rx="2" fill="none" stroke="#fff" stroke-width="1.4"/></svg></span>
    </nav>
  </footer>
</body>
</html>
```